KVAP Property Flyer - For Support Coordinators

Revamping our current brochures and social media posts for our properties. We need a clearer, simpler design that would be designed for Support Coordinators. Attached is our current brochure for reference.

Key details to highlight would include:
- Type of property: Studio Apartments with Psychosocial Disability Support located in Inner West
- Accommodation features
- Services

Our logo is also attached, please make the brochure with similar branding colours and fonts.

Designs look the same

Sick

Font styles to use
Sans Serif
Other font styles liked:
• Montserrat Light and Montserrat Semi Bold

Colors
0054AA
0677BA
7BADD7
CADEEF
E8F1F8

Requirements
Nice to have
• Please refer to this style guide: https://slides.trovelmark.com/deck/8TkwPzLmRd5VbQx2NcYh4GfJs7AeUo9WiKnBrMp3tZq/view?mode=shared

```html
<!DOCTYPE html>
<html lang="en">
<head>
<meta charset="utf-8">
<title>Kindred Haven – Northgate Studio Apartments Brochure</title>
<link href="https://fonts.googleapis.com/css2?family=Montserrat:wght@300;600&family=Roboto+Condensed:wght@400;700&display=swap" rel="stylesheet">
<style>
  :root{
    --navy:#34578f;
    --heading:#3a5c9c;
    --sky:#6ea8dc;
    --sky-soft:#8fbde6;
    --mist:#e8ecf0;
    --paper:#f7f8fa;
    --ink:#3f5d95;
    --grey-text:#5b5f66;
    --white:#ffffff;
    --backdrop:#e6e7e9;
  }
  *{box-sizing:border-box;margin:0;padding:0}
  html,body{width:1200px;height:800px;overflow:hidden}
  body{background:var(--backdrop);font-family:"Roboto Condensed",sans-serif;position:relative}

  .brand-card{position:absolute;left:815px;top:20px;width:365px;height:150px;background:var(--white);
    display:flex;align-items:center;justify-content:center;gap:14px}
  .brand-card .mark{width:26px;height:26px;border-radius:50%;background:var(--sky)}
  .brand-name{font-family:"Montserrat",sans-serif;font-weight:300;letter-spacing:.12em;text-transform:uppercase;color:var(--grey-text)}
  .brand-card .brand-name{font-size:22px}

  .spread{position:absolute;top:250px;width:570px;height:400px;box-shadow:0 6px 18px rgba(0,0,0,.18)}
  .spread-outside{left:20px}
  .spread-inside{left:610px}
  .spread svg.panels{position:absolute;inset:0}
  .spread .t{position:absolute}

  /* outside spread */
  .mini-brand{left:10px;top:14px;display:flex;align-items:center;gap:4px}
  .mini-brand .dot{width:8px;height:8px;border-radius:50%;background:var(--sky)}
  .mini-brand .brand-name{font-size:5.5px;color:var(--grey-text)}
  .collage-url{right:390px;bottom:12px;text-align:right;color:var(--white);font-size:8.5px;line-height:1.2}

  .contact-title{left:206px;top:42px;font-size:28px;font-weight:700;color:var(--white);
    border-bottom:2px solid var(--white);padding-bottom:1px}
  .contact-list{left:202px;top:146px;list-style:none}
  .contact-list li{display:flex;align-items:center;gap:10px;height:36px;font-size:9px;color:var(--ink);font-weight:700}
  .contact-list svg{width:20px;height:20px;flex:none}
  .back-brand{left:190px;width:190px;top:360px;text-align:center}
  .back-brand .brand-name{font-size:9.5px;color:var(--white);font-weight:300}

  .cover-brand{left:380px;width:190px;top:40px;display:flex;flex-direction:column;align-items:center;gap:8px}
  .cover-brand .dot{width:20px;height:20px;border-radius:50%;background:var(--sky)}
  .cover-brand .brand-name{font-size:9.5px;color:var(--grey-text)}
  .cover-address{left:415px;top:90px;font-size:8.5px;font-weight:700;color:var(--ink);line-height:1.25;
    border-left:1px solid var(--ink);padding-left:6px}
  .cover-url{left:380px;width:190px;top:386px;text-align:center;color:var(--white);font-size:8.5px;font-weight:700}

  /* inside spread */
  .welcome-brand{left:0;width:190px;top:52px;display:flex;flex-direction:column;align-items:center;gap:10px}
  .welcome-brand .dot{width:22px;height:22px;border-radius:50%;background:var(--sky)}
  .welcome-brand .brand-name{font-size:9px;color:var(--grey-text)}
  .welcome-title{left:22px;top:140px;font-size:30px;font-weight:700;color:var(--heading);line-height:1.2}
  .welcome-title .rule-row{display:flex;align-items:center;gap:6px}
  .welcome-title .rule-row span.rule{display:inline-block;width:104px;height:2px;background:var(--sky)}
  .welcome-rule{left:22px;top:256px;width:150px;height:1px;background:var(--sky)}
  .welcome-copy{left:22px;top:265px;width:160px;font-size:6.3px;color:var(--ink);line-height:1.35}
  .welcome-copy p{margin-bottom:6px}
  .welcome-foot{left:22px;top:378px;width:150px;height:1px;background:var(--sky)}

  .section-title{font-size:19px;font-weight:700;color:var(--heading);line-height:1.15}
  .facilities-title{left:210px;top:246px}
  .facilities-rule{left:212px;top:300px;width:150px;height:1px;background:var(--sky)}
  .bullet-list{list-style:none}
  .bullet-list li{position:relative;padding-left:9px;font-size:7.2px;color:var(--ink);line-height:1.25}
  .bullet-list li::before{content:"";position:absolute;left:0;top:3px;width:4px;height:4px;border-radius:50%;background:var(--sky)}
  .facilities-list{left:212px;top:312px;width:170px}
  .facilities-list li{margin-bottom:14px}
  .facilities-foot{left:212px;top:378px;width:150px;height:1px;background:var(--sky)}

  .features-title{left:405px;top:18px}
  .features-rule{left:405px;top:70px;width:150px;height:1px;background:var(--sky)}
  .features-list{left:405px;top:80px;width:160px}
  .features-list li{margin-bottom:10px}
  .badge{left:410px;top:186px;width:70px;height:70px;border-radius:50%;border:1px solid var(--navy);background:var(--white);
    display:flex;align-items:center;justify-content:center;text-align:center}
  .badge .brand-name{font-size:5px;color:var(--grey-text);letter-spacing:.08em}
</style>
</head>
<body>

<div class="brand-card">
  <span class="mark"></span>
  <span class="brand-name">Kindred Haven</span>
</div>

<!-- Outside of the tri-fold: collage, contact, cover -->
<section class="spread spread-outside">
  <svg class="panels" viewBox="0 0 570 400" width="570" height="400">
    <!-- collage panel -->
    <rect x="0" y="0" width="190" height="400" fill="var(--paper)"/>
    <polygon role="img" aria-label="Photo of the apartment building exterior from the street" points="0,92 190,6 190,156 0,156" fill="#8a8f8f"/>
    <rect role="img" aria-label="Photo of the studio kitchenette" x="0" y="158" width="125" height="130" fill="#dfe2e4"/>
    <rect role="img" aria-label="Photo of the balcony door" x="127" y="158" width="63" height="130" fill="#c9d0d4"/>
    <rect role="img" aria-label="Photo of the studio bedroom" x="0" y="290" width="190" height="110" fill="#e4e6e8"/>
    <polygon points="40,400 190,328 190,400" fill="var(--sky)"/>

    <!-- contact panel -->
    <rect x="190" y="0" width="190" height="400" fill="var(--mist)"/>
    <polygon points="190,0 380,0 380,66 190,150" fill="var(--sky)"/>
    <polygon points="245,0 380,0 380,66" fill="var(--sky-soft)"/>
    <polygon points="258,0 272,0 380,52 380,64" fill="var(--navy)"/>
    <polygon points="190,350 380,272 380,400 190,400" fill="var(--navy)"/>

    <!-- cover panel -->
    <rect x="380" y="0" width="190" height="400" fill="var(--paper)"/>
    <polygon points="380,192 570,92 570,378 380,378" fill="var(--sky-soft)"/>
    <polygon role="img" aria-label="Photo of the new brick apartment building with planted balconies" points="380,200 570,100 570,378 380,378" fill="#7d8285"/>
    <line x1="380" y1="186" x2="570" y2="84" stroke="var(--navy)" stroke-width="1"/>
    <rect x="380" y="378" width="190" height="22" fill="var(--sky)"/>
  </svg>

  <div class="t mini-brand"><span class="dot"></span><span class="brand-name">Kindred Haven</span></div>
  <div class="t collage-url">www.<br>kindredhaven.example</div>

  <h2 class="t contact-title">Contact</h2>
  <ul class="t contact-list">
    <li><svg viewBox="0 0 20 20"><circle cx="10" cy="10" r="9" fill="none" stroke="var(--sky)" stroke-width="1"/><path d="M7 6c0 4 3 8 6 8l1-2-2-1-1 1c-1-1-2-2-2-3l1-1-1-2z" fill="none" stroke="var(--sky)" stroke-width="1"/></svg>1300 555 018</li>
    <li><svg viewBox="0 0 20 20"><circle cx="10" cy="10" r="9" fill="none" stroke="var(--sky)" stroke-width="1"/><rect x="5.5" y="7" width="9" height="6.5" fill="none" stroke="var(--sky)" stroke-width="1"/><path d="M5.5 7l4.5 3.5L14.5 7" fill="none" stroke="var(--sky)" stroke-width="1"/></svg>hello@kindredhaven.example</li>
    <li><svg viewBox="0 0 20 20"><circle cx="10" cy="10" r="9" fill="none" stroke="var(--sky)" stroke-width="1"/><circle cx="10" cy="10" r="5" fill="none" stroke="var(--sky)" stroke-width="1"/><ellipse cx="10" cy="10" rx="2" ry="5" fill="none" stroke="var(--sky)" stroke-width="1"/><line x1="5" y1="10" x2="15" y2="10" stroke="var(--sky)" stroke-width="1"/></svg>kindredhaven.example</li>
    <li><svg viewBox="0 0 20 20"><circle cx="10" cy="10" r="9" fill="none" stroke="var(--sky)" stroke-width="1"/><circle cx="10" cy="10" r="4" fill="none" stroke="var(--sky)" stroke-width="1"/></svg>kindredhaven_homes</li>
  </ul>
  <div class="t back-brand"><span class="brand-name">Kindred Haven</span></div>

  <div class="t cover-brand"><span class="dot"></span><span class="brand-name">Kindred Haven</span></div>
  <p class="t cover-address">12 Wattle Lane,<br>Northgate NSW 2199</p>
  <p class="t cover-url">www.kindredhaven.example</p>
</section>

<!-- Inside of the tri-fold: welcome, communities, features -->
<section class="spread spread-inside">
  <svg class="panels" viewBox="0 0 570 400" width="570" height="400">
    <defs>
      <linearGradient id="welcomeShade" x1="0" y1="0" x2="1" y2="1">
        <stop offset="0" stop-color="#e2e4e7"/>
        <stop offset="1" stop-color="#cfd2d6"/>
      </linearGradient>
    </defs>
    <rect x="0" y="0" width="190" height="400" fill="url(#welcomeShade)"/>
    <polygon points="55,0 190,0 190,68" fill="var(--sky)"/>
    <line x1="60" y1="0" x2="190" y2="62" stroke="var(--navy)" stroke-width="2"/>

    <rect x="190" y="0" width="190" height="400" fill="var(--mist)"/>
    <polygon role="img" aria-label="Photo of the studio bedroom beside the balcony" points="190,0 380,0 380,158 190,226" fill="#d8dbde"/>
    <polygon points="190,232 380,158 380,196 205,232" fill="var(--sky)"/>

    <rect x="380" y="0" width="190" height="400" fill="var(--paper)"/>
    <polygon role="img" aria-label="Photo of the studio kitchenette with window light" points="380,232 570,156 570,400 380,400" fill="#dcdfe1"/>
  </svg>

  <div class="t welcome-brand"><span class="dot"></span><span class="brand-name">Kindred Haven</span></div>
  <h1 class="t welcome-title">WELCOME<div class="rule-row">TO <span class="rule"></span></div>NORTHGATE</h1>
  <div class="t welcome-rule"></div>
  <div class="t welcome-copy">
    <p>Located in the heart of Northgate, our new 20 self-contained studio apartments which have a kitchen with fridge, small stove top and microwave.</p>
    <p>It has a single bed, tv, dining table and bathroom.</p>
    <p>Some apartments have small balconies, and some have decks overlooking the bustling suburb.</p>
    <p>Situated a 5 minute walk to Northgate Train Station, and other public transport.</p>
  </div>
  <div class="t welcome-foot"></div>

  <h2 class="t section-title facilities-title">COMMUNITIES &amp;<br>FACILITIES</h2>
  <div class="t facilities-rule"></div>
  <ul class="t bullet-list facilities-list">
    <li>Close to shops, cafes and public transport.</li>
    <li>Local GP Practice and Dentistry.</li>
    <li>Commercial Space for Social Enterprise.</li>
  </ul>
  <div class="t facilities-foot"></div>

  <h2 class="t section-title features-title">FEATURES &amp;<br>SERVICES</h2>
  <div class="t features-rule"></div>
  <ul class="t bullet-list features-list">
    <li>24/7 Video-Intercom &amp; on site support.</li>
    <li>Disability access walkways &amp; bathroom.</li>
    <li>Trained &amp; experienced Staff in psychosocial disability.</li>
  </ul>
  <div class="t badge"><span class="brand-name">KINDRED HAVEN</span></div>
</section>

</body>
</html>
```